Website Design for my CNC machine Shop.

I need a new website for my Machining Company.

It can be a simple website that acts more like an "Online Business card" I has to highlight the services I provide and give Companies the confidence to engage my services.

I needs it to be a really modern or even a little futuristic promoting my Company.

I have just moved locations and have renovated the premises and would be great to let everyone know along with a new website.

If you can help with linking it to search engines to help get more exposure that would be great.

It needs to accommodate the three main services I provide which will include capacities of each machine (within that service) and maybe a couple images.
CNC Machining (5-axis, 3-axis)
EDM Wire cutting
3D Metal Printing
Along with home page and Contact page

I have two websites and you can use the txt from either/combination of these.
www.korvaltooling.com.au
(no longer do Laser Marking and etching but now do 3D metal Printing)
www.tarnquill.com.au

Happy to chat further with the designer

Company logo's provided.

For Images: I am happy to use Glimmerbay and can purchase any images you like
EDM Wire cut
https://www.glimmerbay-pics.com/search/edm-wire-cutting

CNC Machining:
https://www.glimmerbay-pics.com/search/vertical-cnc-machining
Don't use any with engines or motor vehicle parts

3D metal Printing
https://www.glimmerbay-pics.com/search/slm-metal-printing

Target Market(s)

Defence, Aerospace, Medical, HIgh Precision

Industry/Entity Type

Mechanical Engineering

Coding

Coded - Design and coding required

Number of Pages Required

5+ page

Requirements
Must have
• Home page, 3 services, Contacts. Can add image to each of the services

```html
<!DOCTYPE html>
<html lang="en">
<head>
<meta charset="utf-8">
<title>Korval Engineering – Precision Machinists</title>
<link rel="stylesheet" href="https://fonts.googleapis.com/css2?family=Poppins:wght@300;400;500;600;700;800&family=Mulish:wght@400;600;700&display=swap">
<style>
:root{
  --navy:#0a2839;
  --navy-deep:#072030;
  --panel:#0e3a52;
  --green:#2db37a;
  --white:#ffffff;
  --ink:#1c2a33;
  --grey:#6b7780;
  --line:#c9d0d5;
}
*{box-sizing:border-box;margin:0;padding:0}
html,body{width:1200px;height:4669px;overflow:hidden}
body{font-family:"Mulish",sans-serif;color:var(--ink);background:var(--white);position:relative}
section,header,footer,.top-bar{position:absolute;left:0;width:1200px}
.abs{position:absolute}
.heading{font-family:"Poppins",sans-serif;font-weight:300;text-transform:uppercase;letter-spacing:.5px}
.heading b{font-weight:800}
.eyebrow{font-family:"Poppins",sans-serif;font-size:15px;text-transform:uppercase;letter-spacing:.3px}
.btn{display:flex;align-items:center;justify-content:center;gap:7px;background:var(--green);color:var(--white);font-family:"Poppins",sans-serif;font-weight:600;font-size:13px;text-transform:uppercase}
.btn i{width:9px;height:9px;border-radius:50%;background:var(--white);display:inline-block;position:relative}
.btn i::after{content:"";position:absolute;left:2px;top:3px;border-left:4px solid var(--green);border-top:1.5px solid transparent;border-bottom:1.5px solid transparent}
.center{left:0;width:1200px;text-align:center}

/* top bar */
.top-bar{top:0;height:29px;background:var(--navy);color:var(--white);font-size:12px}
.top-bar .contact-item{top:7px;display:flex;align-items:center;gap:6px}
.top-bar .follow{left:879px;top:0;width:321px;height:29px}
.top-bar .follow-text{left:964px;top:7px;font-size:12px}
.sq{width:13px;height:13px;border:2px solid var(--white);border-radius:2px;display:block}

/* header */
.site-header{top:29px;height:73px;background:var(--white);box-shadow:0 1px 3px rgba(0,0,0,.08)}
.brand{left:67px;top:18px;display:flex;align-items:center;gap:8px;font-family:"Poppins",sans-serif;font-weight:700;font-size:32px;color:#6f7c86;letter-spacing:2px}
.brand .mark{width:10px;height:10px;background:var(--green)}
.nav{top:31px;font-family:"Poppins",sans-serif;font-size:12.5px;text-transform:uppercase;color:var(--ink)}
.nav.active{color:var(--green)}

/* hero */
.hero{top:102px;height:609px;overflow:hidden}
.hero-photo{left:0;top:0;width:1200px;height:609px;background:linear-gradient(90deg,#0d2a38 0%,#1d3a48 35%,#5e625c 62%,#b59c6a 80%,#3b3e3c 100%)}
.hero .eyebrow{left:67px;top:160px;color:var(--white);font-size:20px;font-weight:400}
.hero h1{left:67px;top:192px;color:var(--white);font-family:"Poppins",sans-serif;font-weight:800;font-size:45px;line-height:56px;text-transform:uppercase}
.hero p{left:67px;top:320px;width:470px;color:var(--white);font-size:16px;line-height:27px}
.hero .btn{left:67px;top:397px;width:145px;height:45px}

/* welcome */
.welcome{top:711px;height:750px}
.welcome-photo{left:67px;top:121px;width:479px;height:479px;background:radial-gradient(circle at 70% 45%,#f2c26a 0%,#b8733a 12%,#2f4c69 35%,#0c1a2c 80%)}
.welcome-frame{left:546px;top:121px;width:25px;height:508px;background:var(--navy)}
.edm-panel{left:181px;top:476px;width:390px;height:153px;background:var(--navy);padding:24px 20px;color:var(--white)}
.edm-panel h3{font-family:"Poppins",sans-serif;font-weight:600;font-size:21px;text-transform:uppercase}
.edm-panel h3 span{color:var(--green)}
.edm-panel p{margin-top:10px;font-size:13.5px;line-height:22px;color:#dfe6ea}
.welcome .eyebrow{left:629px;top:196px;font-size:15px}
.welcome h2{left:629px;top:222px;font-size:44px;color:var(--ink)}
.welcome .lead{left:629px;top:303px;width:500px;font-size:15px;line-height:25px;color:var(--ink)}
.welcome .body{left:629px;top:365px;width:505px;font-size:15px;line-height:26px;color:var(--grey)}
.welcome .btn{left:629px;top:504px;width:143px;height:45px}

/* services */
.services{top:1461px;height:760px;background:var(--navy);color:var(--white)}
.services .eyebrow{top:78px}
.services h2{top:104px;font-size:44px}
.services .sub{top:177px;font-size:16px}
.service-card{top:245px;width:341px;height:433px}
.service-photo{left:0;top:0;width:326px;height:285px}
.service-panel{left:33px;top:285px;width:308px;height:148px;background:var(--panel);padding:18px 16px}
.service-panel h3{font-family:"Poppins",sans-serif;font-weight:600;font-size:19px;text-transform:uppercase}
.service-panel h3 span{color:var(--green)}
.service-panel p{margin-top:12px;font-size:13px;line-height:22px;color:#dfe6ea}
.arrow-box{right:0;bottom:0;width:31px;height:31px;background:var(--green);display:flex;align-items:center;justify-content:center}

/* projects */
.projects{top:2221px;height:861px}
.projects .eyebrow{top:115px}
.projects h2{top:141px;font-size:44px}
.tile{overflow:hidden}
.tile-label{left:0;top:103px;width:348px;text-align:center;color:var(--white);font-family:"Poppins",sans-serif;text-transform:uppercase}

/* blog */
.blog{top:3082px;height:595px;background:var(--navy);color:var(--white)}
.blog .eyebrow{top:69px}
.blog h2{top:95px;font-size:44px}
.blog-card{top:178px;width:341px;height:351px;background:var(--panel)}
.blog-photo{left:0;top:0;width:320px;height:199px}
.blog-card h3{left:12px;top:217px;font-family:"Poppins",sans-serif;font-weight:600;font-size:18.5px;line-height:26px;text-transform:uppercase}
.blog-card .btn{left:14px;top:284px;width:143px;height:45px}

/* contact */
.contact{top:3677px;height:529px;overflow:hidden}
.contact .eyebrow{left:67px;top:127px}
.contact h2{left:67px;top:153px;font-size:44px}
.field{border:1px solid var(--line);background:var(--white);font-size:12px;padding:13px 10px;color:var(--ink)}
.contact .btn{left:67px;top:346px;width:290px;height:49px;font-weight:500}

/* footer */
.site-footer{top:4206px;height:463px;background:var(--navy-deep);color:var(--white)}
.site-footer .brand{left:67px;top:68px;color:#dfe6ea;font-size:40px}
.divider{top:66px;width:2px;height:34px;background:var(--green)}
.col-title{top:68px;font-family:"Poppins",sans-serif;font-weight:600;font-size:15px;color:var(--green);text-transform:uppercase}
.footer-link{font-size:12.5px;color:#d5dde2}
.info-row{left:67px;display:flex;align-items:flex-start;gap:14px;font-size:12.5px;line-height:22px;color:#d5dde2}
.info-icon{width:33px;height:33px;background:var(--green);display:flex;align-items:center;justify-content:center;flex:none}
.social-box{top:112px;width:33px;height:33px;border:1px solid #5b7180;display:flex;align-items:center;justify-content:center}
.social-box span{width:11px;height:11px;background:var(--white)}
.footer-rule{left:0;top:380px;width:1200px;height:1px;background:#1b3a4c}
.copyright{top:408px;font-size:12px;color:#d5dde2}
.copyright b{color:var(--green);font-weight:600}
</style>
</head>
<body>

<div class="top-bar">
  <div class="abs contact-item" style="left:67px">
    <svg width="9" height="11" viewBox="0 0 10 12"><path d="M2 0l2 3-1 1.5c.6 1.5 1.8 2.8 3.2 3.5L7.7 7 10 9.5 8.5 11.5C4 11 0 6 0 1.5z" fill="#2db37a"/></svg>
    +61 400 555 217
  </div>
  <div class="abs contact-item" style="left:207px">
    <svg width="12" height="9" viewBox="0 0 12 9"><rect width="12" height="9" fill="#2db37a"/><path d="M0 0l6 5 6-5" stroke="#0a2839" fill="none"/></svg>
    info@korvaltooling.com.au
  </div>
  <svg class="abs follow" viewBox="0 0 321 29"><polygon points="0,0 321,0 321,29 30,29" fill="#2db37a"/></svg>
  <div class="abs follow-text">Follow Us</div>
  <span class="abs sq" style="left:1038px;top:8px"></span>
  <span class="abs sq" style="left:1077px;top:8px"></span>
  <span class="abs sq" style="left:1118px;top:8px"></span>
</div>

<header class="site-header">
  <div class="abs brand">KORVAL<span class="mark"></span></div>
  <nav>
    <a class="abs nav active" style="left:471px">Home</a>
    <a class="abs nav" style="left:547px">EDM Wire Cutting</a>
    <a class="abs nav" style="left:707px">CNC Machining</a>
    <a class="abs nav" style="left:847px">Laser Marking and Etching</a>
    <a class="abs nav" style="left:1075px">Contact</a>
  </nav>
</header>

<section class="hero">
  <div class="abs hero-photo" role="img" aria-label="Workshop drill press above a vice with scattered bolts and nuts"></div>
  <div class="abs eyebrow">Specialise in</div>
  <h1 class="abs">Technical and<br>creative engineering</h1>
  <p class="abs">Our core sectors of expertise are in EDM wire cutting, Laser Etching/Marking and CNC machining.</p>
  <a class="abs btn">Read more <i></i></a>
</section>

<section class="welcome">
  <div class="abs welcome-frame"></div>
  <div class="abs welcome-photo" role="img" aria-label="Welder at work with bright sparks in a dark workshop"></div>
  <div class="abs edm-panel">
    <h3><span>EDM</span> Services</h3>
    <p>We provide a range of speciality services to a broad range of customers in the Automotive, Aerospace and Defence Industries.</p>
  </div>
  <div class="abs eyebrow">Welcome to</div>
  <h2 class="abs heading"><b>Korval</b> Engineering</h2>
  <p class="abs lead">We are an innovative company that specialise in technical and creative engineering</p>
  <p class="abs body">Our core sectors of expertise are in EDM wire cutting, Laser Etching/Marking and CNC machining. With our combination of highly skilled staff and sophisticated machinery we offer a comprehensive and professional service.</p>
  <a class="abs btn">Read more <i></i></a>
</section>

<section class="services">
  <div class="abs center eyebrow">What we do</div>
  <h2 class="abs center heading"><b>Our</b> Services</h2>
  <p class="abs center sub">Being a high precision engineering company we offer a range of high qualtiy services to a veriaty of industries.</p>

  <article class="abs service-card" style="left:67px">
    <div class="abs service-photo" style="background:linear-gradient(160deg,#2a5a80,#5b7f9c 45%,#1c3346)" role="img" aria-label="Vertical CNC mill cutting metal with coolant spray"></div>
    <div class="abs service-panel">
      <h3><span>CNC</span> Machining</h3>
      <p>With our combination of high quality Torvane Machining Centres we are able to provide...</p>
      <div class="abs arrow-box"><svg width="12" height="10" viewBox="0 0 12 10"><path d="M0 5h10M6 1l4 4-4 4" stroke="#fff" stroke-width="1.6" fill="none"/></svg></div>
    </div>
  </article>
  <article class="abs service-card" style="left:430px">
    <div class="abs service-photo" style="background:linear-gradient(160deg,#5d6b74,#b9c0c4 50%,#3d474d)" role="img" aria-label="EDM wire cutting head over a metal workpiece"></div>
    <div class="abs service-panel">
      <h3><span>EDM</span> Wire Cutting</h3>
      <p>We operate Swiss manufactured Velmont EDM Machines which are regarded as the Aldermere...</p>
      <div class="abs arrow-box"><svg width="12" height="10" viewBox="0 0 12 10"><path d="M0 5h10M6 1l4 4-4 4" stroke="#fff" stroke-width="1.6" fill="none"/></svg></div>
    </div>
  </article>
  <article class="abs service-card" style="left:790px">
    <div class="abs service-photo" style="background:linear-gradient(160deg,#e6e8ea,#a9aeb2 50%,#6d7378)" role="img" aria-label="3D printed metal parts with lattice structures"></div>
    <div class="abs service-panel">
      <h3><span>3D</span> Metal Printing</h3>
      <p>Opertating our brand new CNC Hanvik Lathe with Live tooling makes most Turning jobs a breeze...</p>
      <div class="abs arrow-box"><svg width="12" height="10" viewBox="0 0 12 10"><path d="M0 5h10M6 1l4 4-4 4" stroke="#fff" stroke-width="1.6" fill="none"/></svg></div>
    </div>
  </article>
</section>

<section class="projects">
  <div class="abs center eyebrow">Portfolio</div>
  <h2 class="abs center heading"><b>Our</b> Projects</h2>
  <div class="abs tile" style="left:67px;top:236px;width:348px;height:246px;background:linear-gradient(135deg,#3b3a36,#6a6258 50%,#2a2a28)" role="img" aria-label="Laser etched metal fitting">
    <div class="abs tile-label"><div style="font-size:12px;font-weight:600">Laser</div><div style="font-size:19px;font-weight:600">Marking &amp; Etching</div></div>
  </div>
  <div class="abs tile" style="left:426px;top:236px;width:348px;height:502px;background:linear-gradient(160deg,#8a5c38,#b88456 45%,#6e4a2e)" role="img" aria-label="Engraved metal discs on a wooden table"></div>
  <div class="abs tile" style="left:785px;top:236px;width:348px;height:246px;background:linear-gradient(135deg,#d4d6d6,#7d8080 50%,#e2e3e3)" role="img" aria-label="Laser marked metal brackets in a row"></div>
  <div class="abs tile" style="left:67px;top:491px;width:348px;height:247px;background:linear-gradient(160deg,#e9ecef,#c8ccd1 60%,#2c2f33)" role="img" aria-label="Engraved metal tags on a white surface"></div>
  <div class="abs tile" style="left:785px;top:491px;width:348px;height:247px;background:linear-gradient(135deg,#f1f1f1,#c9cbcc 55%,#ededed)" role="img" aria-label="Machined aluminium clamp part"></div>
</section>

<section class="blog">
  <div class="abs center eyebrow">Blog post</div>
  <h2 class="abs center heading"><b>Recent</b> Blog</h2>
  <article class="abs blog-card" style="left:67px">
    <div class="abs blog-photo" style="background:linear-gradient(160deg,#1f3442,#7b8a94 55%,#d9dde0)" role="img" aria-label="Laser cutting a serrated steel sheet"></div>
    <h3 class="abs">Duis aute irure dolor in<br>reprehenderit</h3>
    <a class="abs btn">Read more <i></i></a>
  </article>
  <article class="abs blog-card" style="left:430px">
    <div class="abs blog-photo" style="background:linear-gradient(160deg,#15191c,#55606a 50%,#1a1f22)" role="img" aria-label="Lathe turning a metal shaft"></div>
    <h3 class="abs">Duis aute irure dolor in<br>reprehenderit</h3>
    <a class="abs btn">Read more <i></i></a>
  </article>
  <article class="abs blog-card" style="left:792px">
    <div class="abs blog-photo" style="background:radial-gradient(circle at 50% 60%,#f3a54a,#8a4a22 30%,#1b1d20 75%)" role="img" aria-label="Laser cutter throwing sparks off metal"></div>
    <h3 class="abs">Duis aute irure dolor in<br>reprehenderit</h3>
    <a class="abs btn">Read more <i></i></a>
  </article>
</section>

<section class="contact">
  <svg class="abs" style="left:0;top:0" width="1200" height="529" viewBox="0 0 1200 529" role="img" aria-label="CNC machine milling a row of aluminium parts">
    <defs><linearGradient id="contactTone" x1="0" y1="0" x2="1" y2="1"><stop offset="0" stop-color="#2e3e4a"/><stop offset=".5" stop-color="#7d8c96"/><stop offset="1" stop-color="#cfd6da"/></linearGradient></defs>
    <polygon points="925,0 1200,0 1200,529 607,529" fill="url(#contactTone)"/>
  </svg>
  <div class="abs eyebrow">Contact us</div>
  <h2 class="abs heading"><b>Get</b> in touch</h2>
  <div class="abs field" style="left:67px;top:230px;width:290px;height:47px">Name:</div>
  <div class="abs field" style="left:366px;top:230px;width:290px;height:47px">Email:</div>
  <div class="abs field" style="left:67px;top:286px;width:290px;height:47px">Phone:</div>
  <div class="abs field" style="left:366px;top:286px;width:290px;height:109px">Comments:</div>
  <a class="abs btn">Submit</a>
</section>

<footer class="site-footer">
  <div class="abs brand">KORVAL<span class="mark"></span></div>
  <div class="abs info-row" style="top:176px">
    <span class="info-icon"><svg width="11" height="15" viewBox="0 0 11 15"><path d="M5.5 0A5.5 5.5 0 0 0 0 5.5C0 9.5 5.5 15 5.5 15S11 9.5 11 5.5A5.5 5.5 0 0 0 5.5 0z" fill="#fff"/><circle cx="5.5" cy="5.5" r="2" fill="#2db37a"/></svg></span>
    <span>Unit 4, 18 Brenmore Rd, DUNSTAN,<br>VIC 3999</span>
  </div>
  <div class="abs info-row" style="top:241px">
    <span class="info-icon"><svg width="12" height="14" viewBox="0 0 10 12"><path d="M2 0l2 3-1 1.5c.6 1.5 1.8 2.8 3.2 3.5L7.7 7 10 9.5 8.5 11.5C4 11 0 6 0 1.5z" fill="#fff"/></svg></span>
    <span style="padding-top:6px">+61 400 555 217 / 03 9000 3127</span>
  </div>
  <div class="abs info-row" style="top:297px">
    <span class="info-icon"><svg width="15" height="11" viewBox="0 0 12 9"><rect width="12" height="9" fill="#fff"/><path d="M0 0l6 5 6-5" stroke="#2db37a" fill="none"/></svg></span>
    <span style="padding-top:6px">info@korvaltooling.com.au</span>
  </div>

  <div class="abs divider" style="left:426px"></div>
  <div class="abs col-title" style="left:497px">Quick links</div>
  <a class="abs footer-link" style="left:497px;top:114px">Home</a>
  <a class="abs footer-link" style="left:497px;top:149px">Projects</a>
  <a class="abs footer-link" style="left:497px;top:183px">Our Company</a>
  <a class="abs footer-link" style="left:497px;top:218px">Services</a>
  <a class="abs footer-link" style="left:497px;top:251px">Contact Us</a>

  <div class="abs divider" style="left:664px"></div>
  <div class="abs col-title" style="left:722px">Services</div>
  <a class="abs footer-link" style="left:722px;top:114px">CNC Machining</a>
  <a class="abs footer-link" style="left:722px;top:149px">EDM Wire cutting</a>
  <a class="abs footer-link" style="left:722px;top:183px">3D Metal Printing</a>

  <div class="abs divider" style="left:877px"></div>
  <div class="abs col-title" style="left:930px">Follow us</div>
  <div class="abs social-box" style="left:930px"><span></span></div>
  <div class="abs social-box" style="left:975px"><span></span></div>
  <div class="abs social-box" style="left:1021px"><span></span></div>

  <div class="abs footer-rule"></div>
  <div class="abs center copyright">© <b>KORVAL</b>, 2024. ALL RIGHTS RESERVED.</div>
</footer>

</body>
</html>
```